Holvern Incorporated

Holvern is a business that provides consulting, and manages and supplies trades persons in the construction and heavy industries sector. We build, do maintenance, install machinery, and can manage projects or jobs. Would like or prefer more clean, classic designs. Blacks/greys, but open to almost anything.

Target Market(s)

Industrial/Construction/Manufacturing

Industry/Entity Type

Construction Company

Contact Information for Business Card

Clean, business name on the front, possibly have the details on the back, but open to any ideas.

Logo Text

We currently do not have a slogan, open to ideas

Font styles to use
Serif
Sans Serif

Colors

Designer to choose colors to be used in the design.

Requirements
Should not have
• the oval is not my logo, was just an idea. please don't send 20 designs with the oval

```html
<!DOCTYPE html>
<html lang="en">
<head>
<meta charset="utf-8">
<title>Holvern Incorporated – Business Card</title>
<link rel="stylesheet" href="https://fonts.googleapis.com/css2?family=Cinzel:wght@500;600&family=Montserrat:wght@400&display=swap">
<style>
  :root {
    --backdrop: #1e1e20;
    --slate: #65646e;
    --paper: #ffffff;
    --amber: #f2a52b;
    --ink: #5d5c63;
  }
  * { margin: 0; padding: 0; box-sizing: border-box; }
  html, body { width: 1200px; height: 900px; overflow: hidden; }
  body {
    background: var(--backdrop);
    display: flex;
    flex-direction: column;
    align-items: center;
    justify-content: center;
    gap: 40px;
    font-family: "Montserrat", sans-serif;
  }
  .card {
    position: relative;
    width: 560px;
    height: 320px;
    border-radius: 3px;
    overflow: hidden;
    box-shadow: 0 14px 30px rgba(0,0,0,.5);
  }

  /* Front */
  .card--front { background: var(--slate); }
  .front-mark {
    position: absolute;
    left: 50%; top: 50%;
    transform: translate(-50%, -50%);
    width: 290px;
    height: 96px;
    background: var(--paper);
    border-radius: 6px;
    display: flex;
    align-items: center;
    justify-content: center;
  }
  .wordmark {
    font-family: "Cinzel", serif;
    font-weight: 600;
    letter-spacing: 2px;
  }
  .front-mark .wordmark { font-size: 50px; color: var(--slate); }

  /* Back */
  .card--back { background: var(--paper); }
  .back-mark {
    position: absolute;
    left: 34px; top: 30px;
    width: 212px; height: 82px;
    background: var(--slate);
    border-radius: 5px;
    display: flex;
    align-items: center;
    justify-content: center;
  }
  .back-mark .wordmark { font-size: 36px; color: var(--paper); }
  .identity-band {
    position: absolute;
    left: 0; right: 0;
    top: 122px; height: 74px;
    background: var(--slate);
    padding: 10px 0 0 36px;
  }
  .person-name {
    font-family: "Cinzel", serif;
    font-weight: 600;
    font-size: 22px;
    letter-spacing: 2px;
    color: var(--amber);
    line-height: 1;
  }
  .person-role {
    margin-top: 4px;
    font-size: 15px;
    color: var(--paper);
    letter-spacing: .5px;
  }
  .contact-list {
    position: absolute;
    left: 36px; top: 222px;
    list-style: none;
  }
  .contact-list li {
    display: flex;
    align-items: center;
    gap: 10px;
    font-size: 16px;
    color: var(--ink);
    line-height: 26px;
    letter-spacing: .5px;
  }
  .contact-list svg { width: 16px; height: 16px; flex: none; }
</style>
</head>
<body>
  <section class="card card--front" aria-label="Card front">
    <div class="front-mark"><span class="wordmark">HOLVERN</span></div>
  </section>

  <section class="card card--back" aria-label="Card back">
    <div class="back-mark"><span class="wordmark">HOLVERN</span></div>
    <div class="identity-band">
      <p class="person-name">DORIAN VALE</p>
      <p class="person-role">Sales Manager</p>
    </div>
    <ul class="contact-list">
      <li>
        <svg viewBox="0 0 16 16" fill="none" stroke="#f2a52b" stroke-width="1.3" aria-hidden="true">
          <circle cx="8" cy="8" r="6.5"/>
          <path d="M5.6 4.8l1.2 1.6-.7.9c.5 1 1.3 1.8 2.3 2.3l.9-.7 1.6 1.2-.6 1.1c-2.6-.3-4.9-2.6-5.2-5.2z"/>
        </svg>
        555-318-2047
      </li>
      <li>
        <svg viewBox="0 0 16 16" fill="none" stroke="#f2a52b" stroke-width="1.3" aria-hidden="true">
          <rect x="1.5" y="3.5" width="13" height="9" rx="1"/>
          <path d="M1.8 4l6.2 5 6.2-5"/>
        </svg>
        info@holvern.com
      </li>
      <li>
        <svg viewBox="0 0 16 16" fill="none" stroke="#f2a52b" stroke-width="1.3" aria-hidden="true">
          <circle cx="8" cy="8" r="6.5"/>
          <ellipse cx="8" cy="8" rx="2.8" ry="6.5"/>
          <path d="M1.5 8h13M2.5 4.8h11M2.5 11.2h11"/>
        </svg>
        www.holvern.com
      </li>
    </ul>
  </section>
</body>
</html>
```